Goal Planning Work Sheet

Design a better Goal Planning Worksheet that is fillable

Target Market(s)

People looking to make an important change

Industry/Entity Type

Work

Requirements
Must have
• Fillable pdf form
• Exceptional Design

```html
<!DOCTYPE html>
<html lang="en">
<head>
<meta charset="utf-8">
<title>Stepwise Planner – Goal Planning Worksheet</title>
<link href="https://fonts.googleapis.com/css2?family=Roboto:ital,wght@0,400;0,700;1,400;1,700&family=Roboto+Condensed:wght@400&display=swap" rel="stylesheet">
<style>
  :root{
    --red:#c8102e;
    --red-bright:#ec1c24;
    --red-dark:#8c0a0d;
    --grey-bg:#e6e7e9;
    --grey-chevron:#6d6e70;
    --orange:#f28a1e;
    --orange-soft:#f7b56a;
    --ink:#1a1a1a;
    --white:#ffffff;
  }
  *{margin:0;padding:0;box-sizing:border-box}
  html,body{width:1200px;height:1200px;overflow:hidden}
  body{background:radial-gradient(circle at 50% 50%,#555 0%,#3a3a3a 60%,#2e2e2e 100%);font-family:"Roboto",Arial,sans-serif;position:relative}

  .worksheet{position:absolute;left:80px;top:210px;width:1040px;height:780px;background:var(--grey-bg);overflow:hidden}
  .band{position:absolute;left:0;width:100%;height:14px;background:linear-gradient(90deg,var(--red-dark),var(--red-bright) 50%,var(--red-dark))}
  .band--top{top:0}
  .band--bottom{bottom:0;height:15px}

  .sidebar{position:absolute;left:0;top:14px;width:287px;height:752px}
  .sidebar__header{position:absolute;left:0;top:0;width:287px;height:240px}
  .brand-name{position:absolute;top:18px;left:0;width:287px;text-align:center;font-family:"Roboto",Arial,sans-serif;font-weight:700;color:var(--white);font-size:29px;line-height:31px;letter-spacing:1px}
  .timer-art{position:absolute;left:99px;top:80px;width:90px;height:102px;border-radius:8px;background:radial-gradient(circle at 50% 55%,var(--orange-soft) 0%,var(--orange) 45%,rgba(242,138,30,0) 72%)}

  .tag{position:absolute;background:var(--red);color:var(--white);font-weight:700;font-style:italic;font-size:13px;line-height:20px;padding:0 5px;text-transform:uppercase;box-shadow:0 0 0 1px rgba(255,255,255,.5)}
  .list{position:absolute;list-style:none}
  .list li{position:relative;padding-left:13px}
  .list li::before{content:"";position:absolute;left:0;top:50%;transform:translateY(-50%);border-left:4px solid var(--red);border-top:3px solid transparent;border-bottom:3px solid transparent}

  .strengths{left:10px;top:280px;font-family:"Roboto Condensed",Arial,sans-serif;font-size:7.6px;color:var(--ink);letter-spacing:-.1px}
  .strengths li{height:14.4px;line-height:14.4px;white-space:nowrap}
  .strengths b{color:var(--red);font-family:"Roboto",Arial,sans-serif;font-style:italic;font-weight:700}

  .panel{position:absolute;left:0;width:297px;background:linear-gradient(90deg,var(--red) 0%,var(--red-bright) 40%,var(--red-dark) 100%)}
  .panel .list{left:14px;top:4px;color:var(--white);font-weight:700;font-style:italic;font-size:10.5px}
  .panel .list li{height:15.2px;line-height:15.2px}
  .panel .list li::before{border-left-color:var(--white)}

  .steps{left:14px;top:615px;font-weight:700;font-style:italic;font-size:10px;color:var(--ink)}
  .steps li{height:13.1px;line-height:13.1px}

  .field{position:absolute;left:303px;width:723px}
  .field__label{color:var(--red);font-weight:700;font-style:italic;font-size:13.4px;line-height:16px;padding-left:9px}
  .field__box{background:var(--white);margin-top:3px}
</style>
</head>
<body>
  <main class="worksheet">
    <div class="band band--top"></div>

    <aside class="sidebar">
      <svg class="sidebar__header" viewBox="0 0 287 240" aria-hidden="true">
        <defs>
          <linearGradient id="headerRed" x1="0" y1="0" x2="1" y2="1">
            <stop offset="0" stop-color="#8c0a0d"/>
            <stop offset=".45" stop-color="#e31b23"/>
            <stop offset="1" stop-color="#a80d12"/>
          </linearGradient>
        </defs>
        <polygon points="0,168 143,238 287,168 287,140 143,211 0,140" fill="var(--grey-chevron)"/>
        <polygon points="0,0 287,0 287,138 143,212 0,138" fill="url(#headerRed)"/>
      </svg>
      <h1 class="brand-name">STEPWISE<br>PLANNER</h1>
      <div class="timer-art" role="img" aria-label="Illustration of an orange stopwatch with a heart and brain on its face"></div>

      <div class="tag" style="left:18px;top:252px">Strength Spotting</div>
      <ul class="list strengths">
        <li><b>Wisdom:</b> Cognitive Creativity&nbsp; Curiosity Judgment Love of Learning Perspective</li>
        <li><b>Courage:</b> Bravery Perseverance Honesty Zest</li>
        <li><b>Humanity:</b> Love Kindness Social Intelligence Teamwork</li>
        <li><b>Justice:</b> Fairness Leadership</li>
        <li><b>Temperance:</b> Forgiveness Humility Prudence Self-Regulation</li>
        <li><b>Transcendence:</b> Appreciation Beauty &amp; Excellence Gratitude Hope Humor Spirituality</li>
      </ul>

      <div class="tag" style="left:26px;top:376px;width:56px;text-align:center">Fear</div>
      <div class="panel" style="top:402px;height:64px">
        <ul class="list">
          <li>Fuse To Thoughts and Feelings</li>
          <li>Excessive Thinking</li>
          <li>Attractors Negative Emotional</li>
          <li>Run Away &amp; Avoidance</li>
        </ul>
      </div>

      <div class="tag" style="left:26px;top:480px;width:56px;text-align:center">Dare</div>
      <div class="panel" style="top:506px;height:65px">
        <ul class="list">
          <li>Defuse: Notice, Name, Normalize</li>
          <li>Acceptance: Allow, Appreciate</li>
          <li>Reinforce Skills &amp; Support</li>
          <li>Enjoy Values</li>
        </ul>
      </div>

      <div class="tag" style="left:26px;top:587px;width:204px">Problem Solving Process</div>
      <ul class="list steps">
        <li>Domain of Problem</li>
        <li>Team Gathered</li>
        <li>Values Focus</li>
        <li>Imagine, Move, Be</li>
        <li>Define Problem, Cause, Solutions</li>
        <li>Plan-SMARTER Goals</li>
        <li>Resources &amp; Resourcefulness</li>
        <li>Practice, Rehearse</li>
        <li>Act Communicate</li>
        <li>Evaluate Revise</li>
      </ul>
    </aside>

    <section class="field" style="top:28px">
      <h2 class="field__label">Imagine and Move (Motion Creates Emotion) Being the person I want to be, Values, Character Strengths:</h2>
      <div class="field__box" style="height:86px"></div>
    </section>
    <section class="field" style="top:142px">
      <h2 class="field__label">Specific Small Meaningful Measurable Actionable Attainable Timeline Now:</h2>
      <div class="field__box" style="height:205px"></div>
    </section>
    <section class="field" style="top:378px">
      <h2 class="field__label">Roadblocks Resources Rewards Ramification:</h2>
      <div class="field__box" style="height:129px"></div>
    </section>
    <section class="field" style="top:536px">
      <h2 class="field__label">Team Roles:</h2>
      <div class="field__box" style="height:86px"></div>
    </section>
    <section class="field" style="top:651px">
      <h2 class="field__label">Evaluate, Emotions, Revise, Resilient:</h2>
      <div class="field__box" style="height:86px"></div>
    </section>

    <div class="band band--bottom"></div>
  </main>
</body>
</html>
```